Letterhead Design Project

We have recently updated our corporate logo and are seeking a new letterhead template.

Attached is the new logo and the old letterhead.

PLEASE DO NOT USE OUR EXISTING WEB SITE FOR INSPIRATION as we are redesigning it.

Target Market(s)

Executives, search professionals, technical and scientific professionals

Industry/Entity Type

Seeking

```html
<!DOCTYPE html>
<html lang="en">
<head>
<meta charset="utf-8">
<title>Sequora Letterhead</title>
<link href="https://fonts.googleapis.com/css2?family=Ubuntu:wght@400;500&display=swap" rel="stylesheet">
<style>
  :root {
    --brand-blue: #1590cb;
    --header-grey: #f3f3f3;
    --paper: #ffffff;
    --ink: #555a5d;
    --rule: #9a9a9a;
  }
  * { margin: 0; padding: 0; box-sizing: border-box; }
  html, body { width: 971px; height: 1200px; overflow: hidden; background: var(--paper); }
  .letterhead {
    position: relative;
    width: 971px;
    height: 1200px;
    background: var(--paper);
    font-family: "Ubuntu", sans-serif;
    color: var(--ink);
  }
  .masthead {
    position: absolute;
    left: 0; top: 0;
    width: 100%;
    height: 161px;
    background: var(--header-grey);
  }
  .brand {
    position: absolute;
    left: 58px;
    top: 68px;
    display: flex;
    align-items: center;
    gap: 12px;
  }
  .brand-dot {
    width: 50px; height: 50px;
    border-radius: 50%;
    background: var(--brand-blue);
  }
  .brand-name {
    font-size: 38px;
    font-weight: 500;
    color: var(--brand-blue);
    letter-spacing: -0.5px;
  }
  .masthead-rule {
    position: absolute;
    left: 485px;
    top: 75px;
    width: 1px;
    height: 37px;
    background: var(--rule);
  }
  .address {
    position: absolute;
    left: 511px;
    top: 72px;
    font-size: 15px;
    line-height: 22px;
    font-style: normal;
  }
  .contact-lines {
    position: absolute;
    left: 772px;
    top: 72px;
    list-style: none;
    font-size: 15px;
    line-height: 22px;
  }
  .contact-lines li { display: flex; align-items: center; gap: 9px; }
  .contact-icon { width: 16px; height: 16px; flex: none; }
  .footer-band {
    position: absolute;
    left: 0; bottom: 0;
    width: 100%;
    height: 45px;
    background: var(--brand-blue);
    display: flex;
    align-items: center;
    justify-content: center;
  }
  .web-address {
    color: #ffffff;
    font-size: 17px;
    letter-spacing: 4px;
  }
</style>
</head>
<body>
  <main class="letterhead">
    <header class="masthead">
      <div class="brand">
        <span class="brand-dot"></span>
        <span class="brand-name">Sequora</span>
      </div>
      <span class="masthead-rule"></span>
      <address class="address">
        420 Harbor View Road, Suite 115,<br>
        Lakeford, MA 01699
      </address>
      <ul class="contact-lines">
        <li>
          <svg class="contact-icon" viewBox="0 0 16 16" aria-hidden="true">
            <rect x="4.5" y="1" width="7" height="14" rx="1" fill="none" stroke="#1590cb" stroke-width="1.6"/>
            <rect x="6" y="3" width="4" height="7" fill="#1590cb"/>
          </svg>
          555.014.0100
        </li>
        <li>
          <svg class="contact-icon" viewBox="0 0 16 16" aria-hidden="true">
            <rect x="4" y="1" width="8" height="5" fill="none" stroke="#1590cb" stroke-width="1.4"/>
            <rect x="1" y="6" width="14" height="6" rx="1.5" fill="#1590cb"/>
            <rect x="4" y="12" width="8" height="3" fill="#1590cb"/>
          </svg>
          555.014.0110
        </li>
      </ul>
    </header>
    <footer class="footer-band">
      <span class="web-address">www.sequora.com</span>
    </footer>
  </main>
</body>
</html>
```